Business Card for plovrix

Create a Business Card with an existing logo for plovrix AG. We are a Information Technology company that does consulting and developing SW to automate business processes. The main colors are given from the logo.

Industry/Entity Type

Business

Requirements
Nice to have
• we use a a font style Century Gothic in our documents

```html
<!DOCTYPE html>
<html lang="en">
<head>
<meta charset="utf-8">
<title>plovrix – Business Card</title>
<link href="https://fonts.googleapis.com/css2?family=Questrial&family=Roboto:wght@500;700&display=swap" rel="stylesheet">
<style>
  :root {
    --backdrop: #ece9e4;
    --card: #ffffff;
    --brand-green: #7cc242;
    --brand-green-dark: #5fa82c;
    --brand-blue: #1a8fd8;
    --brand-blue-dark: #1565b8;
    --wordmark: #4a4a4c;
    --name-blue: #1a8fd8;
    --text-dark: #2b2b2d;
    --icon-blue: #1a6fc4;
  }
  * { box-sizing: border-box; margin: 0; padding: 0; }
  html, body {
    width: 1200px; height: 913px; overflow: hidden;
    background: var(--backdrop);
  }
  .canvas {
    position: relative; width: 1200px; height: 913px;
    display: flex; flex-direction: column; align-items: center; justify-content: center; gap: 48px;
  }
  .card {
    position: relative; width: 580px; height: 332px;
    background: var(--card); overflow: hidden;
    box-shadow: 0 6px 18px rgba(0,0,0,0.18);
  }
  /* Front */
  .card-front { display: flex; align-items: center; justify-content: center; }
  .wordmark {
    display: flex; align-items: center; gap: 14px;
    font-family: "Questrial", "Century Gothic", sans-serif;
    color: var(--wordmark);
  }
  .wordmark-dot { border-radius: 50%; background: var(--brand-green); }
  .card-front .wordmark { font-size: 72px; }
  .card-front .wordmark-dot { width: 40px; height: 40px; }
  /* Back */
  .card-bands { position: absolute; inset: 0; width: 100%; height: 100%; }
  .card-back .wordmark {
    position: absolute; top: 52px; right: 44px; font-size: 40px; gap: 10px;
  }
  .card-back .wordmark-dot { width: 22px; height: 22px; }
  .contact {
    position: absolute; left: 40px; top: 118px;
    font-family: "Roboto", Arial, sans-serif;
  }
  .contact-name { color: var(--name-blue); font-weight: 700; font-size: 21px; }
  .contact-role { color: var(--text-dark); font-weight: 700; font-size: 14px; margin-top: 6px; }
  .contact-list { list-style: none; margin-top: 18px; }
  .contact-list li {
    display: flex; align-items: center; gap: 12px;
    font-size: 14px; font-weight: 500; color: var(--text-dark); line-height: 23px;
  }
  .contact-list svg { width: 15px; height: 15px; fill: var(--icon-blue); flex: none; }
  .contact-list .web { font-weight: 700; }
</style>
</head>
<body>
<main class="canvas">
  <section class="card card-front" aria-label="Business card front">
    <div class="wordmark"><span class="wordmark-dot"></span><span>plovrix</span></div>
  </section>

  <section class="card card-back" aria-label="Business card back">
    <svg class="card-bands" viewBox="0 0 580 332" preserveAspectRatio="none" aria-hidden="true">
      <path d="M0 0 H330 C250 6 120 10 0 18 Z" fill="var(--brand-green)"/>
      <path d="M0 0 H200 C130 4 60 7 0 10 Z" fill="var(--brand-blue)"/>
      <path d="M0 332 C160 300 380 240 580 150 V332 Z" fill="var(--brand-green)"/>
      <path d="M0 332 C170 306 390 262 580 196 V226 C400 280 200 318 60 332 Z" fill="var(--brand-blue)"/>
      <path d="M250 332 C380 310 490 282 580 252 V332 Z" fill="var(--brand-blue-dark)"/>
    </svg>

    <div class="wordmark"><span class="wordmark-dot"></span><span>plovrix</span></div>

    <div class="contact">
      <p class="contact-name">Lukas Brenner</p>
      <p class="contact-role">CEO</p>
      <ul class="contact-list">
        <li><svg viewBox="0 0 24 24"><path d="M12 2a7 7 0 0 0-7 7c0 5 7 13 7 13s7-8 7-13a7 7 0 0 0-7-7zm0 9.5A2.5 2.5 0 1 1 12 6.5a2.5 2.5 0 0 1 0 5z"/></svg>Feldweg 7, 5400 Baden, Switzerland</li>
        <li><svg viewBox="0 0 24 24"><path d="M6.6 10.8a15 15 0 0 0 6.6 6.6l2.2-2.2a1 1 0 0 1 1-.25 11.4 11.4 0 0 0 3.6.57 1 1 0 0 1 1 1V20a1 1 0 0 1-1 1A17 17 0 0 1 3 4a1 1 0 0 1 1-1h3.5a1 1 0 0 1 1 1c0 1.25.2 2.45.57 3.57a1 1 0 0 1-.25 1z"/></svg>+41 56 210 48 93</li>
        <li><svg viewBox="0 0 24 24"><path d="M7 2h10a2 2 0 0 1 2 2v16a2 2 0 0 1-2 2H7a2 2 0 0 1-2-2V4a2 2 0 0 1 2-2zm0 3v13h10V5z"/></svg>+41 79 604 27 15</li>
        <li><svg viewBox="0 0 24 24"><path d="M2 5h20v14H2zm2 2v.5l8 5 8-5V7l-8 5z"/></svg>lukas.brenner@plovrix.ch</li>
        <li class="web"><svg viewBox="0 0 24 24"><path d="M12 2a10 10 0 1 0 0 20 10 10 0 0 0 0-20zm6.9 6h-3a15 15 0 0 0-1.4-3.6A8 8 0 0 1 18.9 8zM12 4c.8 1.1 1.5 2.5 1.9 4h-3.8c.4-1.5 1.1-2.9 1.9-4zM4.3 14a8 8 0 0 1 0-4h3.4a16 16 0 0 0 0 4zm.8 2h3a15 15 0 0 0 1.4 3.6A8 8 0 0 1 5.1 16zm3-8h-3a8 8 0 0 1 4.4-3.6A15 15 0 0 0 8.1 8zM12 20c-.8-1.1-1.5-2.5-1.9-4h3.8c-.4 1.5-1.1 2.9-1.9 4zm2.3-6H9.7a14 14 0 0 1 0-4h4.6a14 14 0 0 1 0 4zm.2 5.6A15 15 0 0 0 15.9 16h3a8 8 0 0 1-4.4 3.6zM16.3 14a16 16 0 0 0 0-4h3.4a8 8 0 0 1 0 4z"/></svg>www.plovrix.ch</li>
      </ul>
    </div>
  </section>
</main>
</body>
</html>
```